Small Business Consulting Firm Needs Business Card Design

Need a sleek modern business card with 2 sides matching the colors of our logo. We will be placing these with a mailer we are sending out. These business cards will only ever be given to business owners. We operate helping businesses who are struggling with cash flow or finances. If the green and blue design needs to be moved to the right of "Harborline Crest Consulting" for aesthetic purposes that is ok. We will need an editable file if possible. We would like to include the reps name, email, website, and phone number. For now just use Peter Vance, pvance@harborlinecrest.com, www.harborlinecrest.com, and 833-555-0172.

```html
<!DOCTYPE html>
<html lang="en">
<head>
<meta charset="utf-8">
<title>Harborline Crest Consulting — Business Card</title>
<link href="https://fonts.googleapis.com/css2?family=Lato:wght@400;700&display=swap" rel="stylesheet">
<style>
  :root {
    --stage: #141414;
    --card-dark: #1f2021;
    --card-light: #ffffff;
    --brand-green: #7ab833;
    --brand-green-deep: #5f9426;
    --text-light: #f2f2f2;
    --text-dark: #3a3a3a;
  }
  * { box-sizing: border-box; margin: 0; padding: 0; }
  html, body {
    width: 1200px; height: 912px; overflow: hidden;
    background: var(--stage);
    font-family: "Lato", Arial, sans-serif;
  }
  .card {
    position: absolute;
    left: 290px;
    width: 620px; height: 354px;
    box-shadow: 0 14px 30px rgba(0,0,0,.55);
  }
  .card--front { top: 70px; background: var(--card-dark); }
  .card--back { top: 488px; background: var(--card-light); overflow: hidden; }

  .wordmark {
    position: absolute;
    display: flex; flex-direction: column; align-items: center;
    text-transform: uppercase;
    font-weight: 400;
    font-size: 27px;
    letter-spacing: 3px;
    line-height: 1.25;
    text-align: center;
  }
  .wordmark__square {
    width: 46px; height: 46px;
    background: var(--brand-green);
    margin-bottom: 22px;
  }
  .card--front .wordmark { left: 0; right: 0; top: 92px; color: var(--text-light); }
  .card--back .wordmark { left: 22px; width: 270px; top: 108px; color: var(--text-dark); font-size: 22px; letter-spacing: 2px; }
  .card--back .wordmark__square { width: 38px; height: 38px; margin-bottom: 18px; }

  .contact-panel {
    position: absolute;
    left: 300px; top: 28px;
    width: 286px; height: 288px;
    background: var(--card-dark);
  }
  .icon-band {
    position: absolute;
    left: 276px; top: 118px;
    width: 46px; height: 196px;
  }
  .contact {
    position: absolute;
    left: 346px; top: 58px;
    color: var(--text-light);
    font-size: 14px;
    line-height: 1.3;
  }
  .contact__name { font-size: 22px; font-weight: 700; color: var(--brand-green); }
  .contact__role { font-size: 13px; color: var(--text-light); font-weight: 400; }
  .contact__role::before { content: "|"; color: var(--brand-green); margin: 0 6px 0 4px; font-size: 18px; }
  .contact__line { margin-top: 16px; }
  .contact__line + .contact__line { margin-top: 22px; }
  .contact__address { margin-top: 26px; }
</style>
</head>
<body>

<section class="card card--front" aria-label="Card front">
  <div class="wordmark">
    <span class="wordmark__square"></span>
    <span>Harborline Crest</span>
    <span>Consulting</span>
  </div>
</section>

<section class="card card--back" aria-label="Card back">
  <div class="wordmark">
    <span class="wordmark__square"></span>
    <span>Harborline Crest</span>
    <span>Consulting</span>
  </div>

  <div class="contact-panel"></div>

  <svg class="icon-band" viewBox="0 0 46 196" aria-hidden="true">
    <polygon points="24,0 46,10 46,196 24,186" fill="var(--brand-green)"/>
    <polygon points="0,12 24,0 24,186 0,174" fill="var(--brand-green-deep)"/>
    <g fill="#ffffff">
      <!-- pin -->
      <path d="M34 30 a5 5 0 1 0 -10 0 c0 4 5 9 5 9 s5 -5 5 -9z M29 28 a2 2 0 1 1 0 4 a2 2 0 1 1 0 -4z" fill-rule="evenodd"/>
      <!-- phone -->
      <path d="M25 72 c1 -2 3 -2 4 0 l1 2 c0 1 -1 2 -2 2 c1 3 3 5 6 6 c0 -1 1 -2 2 -2 l2 1 c2 1 2 3 0 4 c-6 2 -14 -6 -13 -13z"/>
      <!-- mail -->
      <rect x="22" y="114" width="16" height="11" rx="1"/>
      <path d="M22 115 l8 6 l8 -6" fill="none" stroke="var(--brand-green)" stroke-width="1.4"/>
      <!-- globe -->
      <circle cx="30" cy="162" r="8"/>
      <g fill="none" stroke="var(--brand-green)" stroke-width="1.1">
        <ellipse cx="30" cy="162" rx="3.5" ry="8"/>
        <line x1="22" y1="162" x2="38" y2="162"/>
        <line x1="30" y1="154" x2="30" y2="170"/>
      </g>
    </g>
  </svg>

  <div class="contact">
    <div><span class="contact__name">Peter Vance</span><span class="contact__role">Manager</span></div>
    <div class="contact__address">418 Marlow Court<br>Dallas, TX 75201</div>
    <div class="contact__line">833-555-0172</div>
    <div class="contact__line">pvance@harborlinecrest.com</div>
    <div class="contact__line">www.harborlinecrest.com</div>
  </div>
</section>

</body>
</html>
```